fieldscoutingpath.com - Social Media Branding

fieldscoutingpath.com --> Social Media Re-Branding & Graphics
Facebook: @fldscoutpath - Instagram: @fieldscoutingpath - Twitter: @fldscoutpath

Looking to find a good designer to help with my fieldscoutingpath.com social media sites!
- facebook banner
- twitter banner
- instagram template (square and banner size)
- Quote or Information Template
- Committed Template (uniformed) - see the ones I made (& i am no professional) at fieldscoutingpath.com/committed - needs to have fieldscoutingpath.com logo, room for: the committed school and the team the player plays on.

Also willing to pay extra for a graphic that is the "complete package" that detail all of the steps of the recruiting process detailed in fieldscoutingpath.com

Font styles to use
Sans Serif

Colors
ec1f27
fbee3e

```html
<!DOCTYPE html>
<html lang="en">
<head>
<meta charset="utf-8">
<title>fieldscoutingpath.com – Talk to an Expert</title>
<link rel="stylesheet" href="https://fonts.googleapis.com/css2?family=Archivo+Black&family=Roboto:wght@400;700&display=swap">
<style>
  :root {
    --brand-red: #ec1f27;
    --brand-yellow: #fbee3e;
    --dirt-light: #a98266;
    --dirt-mid: #8a624a;
    --dirt-dark: #5e3a26;
    --overlay-brown: rgba(96, 44, 16, 0.78);
    --text-light: #ffffff;
    --text-dark: #111111;
    --band-white: #ffffff;
  }
  html, body {
    margin: 0;
    padding: 0;
    overflow: hidden;
    background: var(--band-white);
  }
  .post {
    position: relative;
    width: 1200px;
    height: 1200px;
    overflow: hidden;
    background: var(--band-white);
  }
  .field-photo {
    position: absolute;
    left: 0;
    top: 0;
    width: 1200px;
    height: 1040px;
    background:
      radial-gradient(ellipse at 68% 40%, var(--dirt-light) 0%, var(--dirt-mid) 55%, var(--dirt-dark) 100%);
  }
  .message-disc {
    position: absolute;
    left: 0;
    top: 0;
  }
  .message {
    position: absolute;
    left: 48px;
    top: 266px;
    color: var(--text-light);
  }
  .message__heading {
    margin: 0;
    font-family: "Archivo Black", "Arial Black", sans-serif;
    font-size: 39px;
    line-height: 54px;
    letter-spacing: 0.5px;
  }
  .message__body {
    margin: 6px 0 0 3px;
    font-family: "Roboto", Arial, sans-serif;
    font-size: 42px;
    line-height: 55px;
    font-weight: 400;
  }
  .message__expert {
    font-weight: 700;
  }
  .footer-band {
    position: absolute;
    left: 0;
    top: 1040px;
    width: 1200px;
    height: 160px;
    background: var(--band-white);
  }
  .site-mark {
    position: absolute;
    left: 40px;
    top: 1062px;
    display: flex;
    align-items: center;
  }
  .site-mark__dot {
    width: 130px;
    height: 100px;
    display: block;
  }
  .site-mark__name {
    margin-left: 30px;
    font-family: "Archivo Black", "Arial Black", sans-serif;
    font-size: 38px;
    color: var(--text-dark);
    border-bottom: 3px solid var(--brand-red);
    padding-bottom: 10px;
  }
  .social-handle {
    position: absolute;
    left: 696px;
    top: 1078px;
    display: flex;
    align-items: center;
    font-family: "Archivo Black", "Arial Black", sans-serif;
    font-size: 40px;
    color: var(--brand-red);
  }
  .social-handle__square {
    width: 50px;
    height: 50px;
    background: var(--brand-red);
    border-radius: 8px;
    margin-right: 14px;
  }
</style>
</head>
<body>
  <main class="post">
    <div class="field-photo" role="img" aria-label="Close-up photo of a softball resting on the infield dirt beside a chalked white circle"></div>

    <svg class="message-disc" width="1200" height="1040" viewBox="0 0 1200 1040" aria-hidden="true">
      <circle cx="350" cy="530" r="358" fill="var(--overlay-brown)"/>
    </svg>

    <section class="message">
      <h1 class="message__heading">Have Questions?<br>Want to Talk to an Expert?</h1>
      <p class="message__body">
        Do you have specific questions<br>
        about what college coaches<br>
        look for in an athlete?<br>
        Want recruiting advice from<br>
        a Former Division 1 Coach?<br>
        Spend an hour talking to an<br>
        expert in the industry.<br>
        <span class="message__expert">Dana Whitfield!</span>
      </p>
    </section>

    <footer class="footer-band">
    </footer>

    <div class="site-mark">
      <svg class="site-mark__dot" viewBox="0 0 130 100" aria-hidden="true">
        <circle cx="65" cy="50" r="46" fill="var(--brand-yellow)"/>
      </svg>
      <span class="site-mark__name">fieldscoutingpath.com</span>
    </div>

    <div class="social-handle">
      <span class="social-handle__square" aria-hidden="true"></span>
      <span class="social-handle__name">fieldscoutingpath</span>
    </div>
  </main>
</body>
</html>
```